Book Cover for Herb Growing and Ancient Medecine Recipes for People over 50 years

The front book cover shall
- be an eye-catcher even as small as a thumbnail on a cell phone
- contain the following words:
Title: The Patient Beekeeper
Subtitle: Our detours to Coastal Lanterns
Hook: Effortless fixes for:
• Sleep like never before
• Pain-free movement
• Hair that thrives
• Calm hormones
Author name: Lionel Dravec
- meet Velmora QTL print requirements for size, CMYK colors etc.

Attached are covers of best-selling book in my genre.

Target Market(s)

Velmora book buyers over 50 yrs with some health issues who want to improve their well-being naturally

Colors
00AB8E
00BBA5
67D7C9
C6EFE9
E9F9F6

Requirements
Must have
• a catchy main image

```html
<!DOCTYPE html>
<html lang="en">
<head>
<meta charset="utf-8">
<title>The Patient Beekeeper – Front Cover</title>
<link rel="stylesheet" href="https://fonts.googleapis.com/css2?family=Anton&family=Pinyon+Script&family=Archivo:wght@400;500;700;800&display=swap">
<style>
  :root {
    --teal: #268a84;
    --brown: #3b1f18;
    --paper: #ffffff;
    --stage: #268a84;
    --sketch-light: #f7f3ef;
    --sketch-mid: #e6dbd2;
  }
  * { margin: 0; padding: 0; box-sizing: border-box; }
  html, body {
    width: 1200px; height: 1019px; overflow: hidden;
    background: var(--stage);
  }
  .cover {
    position: absolute; left: 250px; top: 15px;
    width: 700px; height: 989px;
    background: var(--paper);
    font-family: "Archivo", sans-serif;
  }
  .title { font-weight: normal; }
  .title-article {
    position: absolute; top: 56px; left: 0; width: 100%;
    display: block;
    text-align: center;
    font-family: "Pinyon Script", cursive;
    font-size: 72px; line-height: 1; color: var(--brown);
    padding-left: 30px;
  }
  .title-line {
    position: absolute; left: 0; width: 100%;
    display: block;
    text-align: center;
    font-family: "Anton", sans-serif;
    font-weight: 400;
    color: var(--teal); line-height: 1;
    white-space: nowrap;
  }
  .title-line--first { top: 116px; font-size: 76px; letter-spacing: 8px; padding-left: 8px; }
  .title-line--second { top: 184px; font-size: 112px; letter-spacing: 0; }
  .subtitle {
    position: absolute; top: 314px; left: 0; width: 100%;
    text-align: center;
    font-weight: 800; font-size: 21px; line-height: 26px; color: var(--brown);
    text-transform: uppercase; white-space: nowrap;
  }
  .hook {
    position: absolute; top: 355px; left: 124px; width: 450px;
    display: flex; align-items: center; gap: 18px;
    font-size: 14px; line-height: 20px; color: var(--brown); text-transform: uppercase;
    white-space: nowrap;
  }
  .hook::before, .hook::after {
    content: ""; flex: 1; height: 1px; background: var(--teal);
  }
  .benefits {
    position: absolute; top: 398px; left: 110px; width: 480px;
    display: flex; justify-content: center;
    list-style: none;
  }
  .benefit {
    padding: 1px 8px;
    font-size: 14px; line-height: 19px; color: var(--teal);
    text-align: center; text-transform: uppercase; white-space: nowrap;
    border-left: 1px solid var(--brown);
  }
  .benefit:first-child { border-left: none; }
  .benefit--wide { padding: 1px 18px; }
  .main-image {
    position: absolute; left: 175px; top: 497px;
    width: 306px; height: 335px;
    background: radial-gradient(ellipse at 55% 50%, var(--sketch-mid) 0%, var(--sketch-light) 60%, var(--paper) 100%);
  }
  .author {
    position: absolute; top: 897px; left: 131px; width: 432px;
    display: flex; align-items: center; gap: 4px;
    font-weight: 700; font-size: 27px; line-height: 34px; color: var(--teal);
    text-transform: uppercase; letter-spacing: 0.5px; white-space: nowrap;
  }
  .author::before, .author::after {
    content: ""; flex: 1; height: 1px; background: var(--teal);
  }
</style>
</head>
<body>
  <main class="cover">
    <h1 class="title">
      <span class="title-article">The</span>
      <span class="title-line title-line--first">PATIENT</span>
      <span class="title-line title-line--second">BEEKEEPER</span>
    </h1>
    <p class="subtitle">Our detours to Coastal Lanterns</p>
    <p class="hook">Effortless fixes for</p>
    <ul class="benefits">
      <li class="benefit">Sleep like<br>never before</li>
      <li class="benefit">Pain-free<br>movement</li>
      <li class="benefit">Hair that<br>thrives</li>
      <li class="benefit benefit--wide">Calm<br>hormones</li>
    </ul>
    <div class="main-image" role="img" aria-label="Hand-drawn sketch of a mortar and pestle filled with herbs and flowers, with a daisy and berries beside it"></div>
    <p class="author">Lionel Dravec</p>
  </main>
</body>
</html>
```